I want to revise my business card design and get a more modern and up to date design.

Brolvane Handyman Sevices originated from a family-owned and operated contractor business, performing home renovation, addition, and construction work in the NYC area since 2004. Today, we specialize in reliable and affordable handyman services for residential and commercial clients In 2014, we expanded to northern New Jersey. In 2016, we brought quality home improvement and repair services to new Bucks County, PA, and nearby New Jersey areas.
Target Market(s)
Home owners and business that might be looking for a General contractor, handyman, cleaning services and Home maintenance and property.
Industry/Entity Type
Construction Company
Contact Information for Business Card
I am open to new ideas
Colors
Designer to choose colors to be used in the design.
Look and feel
Each slider illustrates characteristics of the customer's brand and the style your logo design should communicate.

```html
<!DOCTYPE html>
<html lang="en">
<head>
<meta charset="UTF-8">
<title>Brolvane Handyman Sevices – Business Card</title>
<link href="https://fonts.googleapis.com/css2?family=Roboto:wght@400;500;900&display=swap" rel="stylesheet">
<style>
  :root{
    --backdrop:#3a3a3c;
    --card-white:#ffffff;
    --card-black:#0c0c0d;
    --ink:#141414;
    --ink-soft:#2b2b2b;
    --brand-red:#e31c25;
    --accent-yellow:#f7c51e;
    --muted-grey:#6d6d6d;
    --light-grey:#d9d9d9;
  }
  *{box-sizing:border-box;margin:0;padding:0}
  html,body{width:1200px;height:900px;overflow:hidden}
  body{
    background:var(--backdrop);
    font-family:'Roboto',Arial,sans-serif;
    display:flex;flex-direction:column;align-items:center;justify-content:center;gap:46px;
  }
  .card{
    width:660px;height:377px;position:relative;
    box-shadow:0 10px 30px rgba(0,0,0,.45);
  }
  .card--front{background:var(--card-white);color:var(--ink)}
  .card--back{background:var(--card-black);display:flex;align-items:center;justify-content:center}

  .brand{position:absolute;left:46px;top:40px}
  .brand__name{font-weight:900;font-size:54px;line-height:1;letter-spacing:-1px;color:var(--ink)}
  .brand__tagline{font-size:13px;letter-spacing:5px;color:var(--muted-grey);margin-top:6px;text-transform:uppercase}

  .person{position:absolute;left:46px;top:162px}
  .person__name{font-size:22px;font-weight:500;color:var(--brand-red);text-transform:uppercase}
  .person__role{font-size:15px;color:var(--ink-soft);margin-top:4px}

  .contact{position:absolute;left:46px;top:232px;list-style:none;font-size:15px;line-height:1.55;color:var(--ink-soft)}
  .contact li{display:flex;align-items:center;gap:8px}
  .contact .address{padding-left:20px}
  .contact svg{width:12px;height:12px;flex:none}

  .emblem-space{
    position:absolute;right:60px;top:92px;width:220px;height:220px;border-radius:50%;
    background:var(--brand-red);
  }

  .back-brand{display:flex;align-items:center;gap:22px}
  .back-brand__mark{width:64px;height:64px;background:var(--brand-red)}
  .back-brand__text{display:flex;flex-direction:column}
  .back-brand__name{font-weight:900;font-size:66px;line-height:1;letter-spacing:-1px;color:var(--light-grey)}
  .back-brand__tagline{font-size:14px;letter-spacing:6px;color:var(--light-grey);margin-top:8px;text-transform:uppercase}
</style>
</head>
<body>
  <section class="card card--front">
    <div class="brand">
      <div class="brand__name">Brolvane</div>
      <div class="brand__tagline">Handyman Services</div>
    </div>

    <div class="person">
      <div class="person__name">Daniel Harrow</div>
      <div class="person__role">Director</div>
    </div>

    <ul class="contact">
      <li class="address">418 Linden Avenue,</li>
      <li class="address">Doylestown, PA, 18901</li>
      <li>
        <svg viewBox="0 0 12 12"><path d="M2.5 1h2l1 3-1.3 1a6 6 0 0 0 2.8 2.8L8 6.5l3 1v2a1.5 1.5 0 0 1-1.5 1.5A8.5 8.5 0 0 1 1 2.5 1.5 1.5 0 0 1 2.5 1z" fill="var(--brand-red)"/></svg>
        (215) 555-0187
      </li>
      <li>
        <svg viewBox="0 0 12 12"><rect x="1" y="2.5" width="10" height="7" fill="none" stroke="var(--brand-red)" stroke-width="1.3"/><path d="M1 2.5l5 4 5-4" fill="none" stroke="var(--brand-red)" stroke-width="1.3"/></svg>
        info@brolvane.com
      </li>
      <li>
        <svg viewBox="0 0 12 12"><circle cx="6" cy="6" r="5" fill="none" stroke="var(--brand-red)" stroke-width="1.3"/><path d="M1 6h10M6 1c2 2.5 2 7.5 0 10M6 1c-2 2.5-2 7.5 0 10" fill="none" stroke="var(--brand-red)" stroke-width="1"/></svg>
        www.brolvane.com
      </li>
    </ul>

    <div class="emblem-space" role="img" aria-label="Brand emblem area"></div>
  </section>

  <section class="card card--back">
    <div class="back-brand">
      <div class="back-brand__mark"></div>
      <div class="back-brand__text">
        <div class="back-brand__name">Brolvane</div>
        <div class="back-brand__tagline">Handyman Services</div>
      </div>
    </div>
  </section>
</body>
</html>
```